Painting Contractor Business Card Design

We are looking for a cool, bold, modern, polished, business card design. We are a high-end residential painting contractor. Please incorporate our logo and keep with our green/black color scheme. We are interested in seeing 2-sided and 1-sided options. Thank you very much!

Industry/Entity Type

Business

Contact Information for Business Card

Info for the card:
Owen Talsky
mobile 206-555-0193
email owen@kestrowfinish.net
web www.kestrowfinish.net

```html
<!DOCTYPE html>
<html lang="en">
<head>
<meta charset="utf-8">
<title>Kestrow Finish – Business Card</title>
<link rel="stylesheet" href="https://fonts.googleapis.com/css2?family=Work+Sans:wght@400;500;600&display=swap">
<style>
  :root {
    --page-bg: #eeece9;
    --card-green: #a6d0a9;
    --ink: #111111;
    --leaf-green: #1f9a3c;
    --leaf-dark: #0d5e24;
    --stripe-black: #101010;
  }
  * { margin: 0; padding: 0; box-sizing: border-box; }
  html, body {
    width: 1200px;
    height: 960px;
    overflow: hidden;
    background: var(--page-bg);
    font-family: "Work Sans", Arial, sans-serif;
    color: var(--ink);
  }
  .sheet {
    width: 1200px;
    height: 960px;
    display: flex;
    flex-direction: column;
    align-items: center;
    justify-content: center;
    gap: 64px;
  }
  .card {
    position: relative;
    width: 560px;
    height: 320px;
    background: var(--card-green);
    overflow: hidden;
  }
  .corner-foliage {
    position: absolute;
    right: 0;
    top: 36px;
    width: 150px;
    height: 170px;
    background: linear-gradient(135deg, var(--leaf-green) 0%, var(--leaf-dark) 55%, var(--stripe-black) 100%);
    opacity: 0.9;
  }
  /* Front */
  .card-front .wordmark-front {
    position: absolute;
    left: 0;
    right: 150px;
    top: 50%;
    transform: translateY(-50%);
    display: flex;
    align-items: center;
    justify-content: center;
    gap: 14px;
    font-weight: 600;
    font-size: 30px;
    letter-spacing: 0.04em;
  }
  .brand-square {
    width: 22px;
    height: 22px;
    background: var(--ink);
  }
  /* Back */
  .card-back .lockup {
    position: absolute;
    left: 34px;
    top: 128px;
    display: flex;
    align-items: center;
    gap: 10px;
    font-weight: 600;
    font-size: 24px;
    letter-spacing: 0.02em;
  }
  .card-back .lockup .brand-square { width: 18px; height: 18px; }
  .contact {
    position: absolute;
    left: 62px;
    top: 172px;
  }
  .contact-name {
    font-size: 26px;
    font-weight: 600;
    line-height: 1.1;
    margin-bottom: 4px;
  }
  .contact-line {
    font-size: 14px;
    font-weight: 500;
    line-height: 1.4;
  }
</style>
</head>
<body>
  <main class="sheet">
    <section class="card card-front" aria-label="Business card front">
      <div class="wordmark-front">
        <span class="brand-square" aria-hidden="true"></span>
        <span>KESTROW FINISH</span>
      </div>
      <div class="corner-foliage" role="img" aria-label="Green grass blades crossing black diagonal stripes"></div>
    </section>

    <section class="card card-back" aria-label="Business card back">
      <div class="lockup">
        <span class="brand-square" aria-hidden="true"></span>
        <span>KESTROW FINISH</span>
      </div>
      <div class="contact">
        <p class="contact-name">Owen Talsky</p>
        <p class="contact-line">Mobile: 206-555-0193</p>
        <p class="contact-line">Email: owen@kestrowfinish.net</p>
        <p class="contact-line">Web: www.kestrowfinish.net</p>
      </div>
      <div class="corner-foliage" role="img" aria-label="Green grass blades crossing black diagonal stripes"></div>
    </section>
  </main>
</body>
</html>
```